Label design, for stand up guayusa tea pouch.

I need a high quality, clean, modern sticker label design. Its going on a stand up tea pouch. The front of the pouch is transparent, with a foil back. The foil back is visible from front view.The product is a dark green herb. its in the form of loose leaf tea. Guayusa provides clean energy. Its main point is that its an alternative to coffee with similar caffeine levels, but it doesn't give the same jittery feeling as coffee because of a component called theobromine.

Target Market(s)

Men and women 18-65

Font styles to use
Sans Serif
Decorative

Colors

Designer to choose colors to be used in the design.

Requirements
Must have
• -Logo provided: icon
• The logo icon colors can be changed to have some green if it will work better
• -Brand: Lanternmoss guayusa
• -A background that goes well with the packaging (transparent/foil) picture provided
Should not have
• Blank background
• Overly loud background

```html
<!DOCTYPE html>
<html lang="en">
<head>
<meta charset="utf-8">
<title>Lanternmoss tea – Guayusa Blend Tea label</title>
<link rel="stylesheet" href="https://fonts.googleapis.com/css2?family=Roboto:wght@500;700&family=Roboto+Condensed:wght@400;500;700&family=Tenor+Sans&family=Dosis:wght@500&display=swap">
<style>
  :root {
    --bg: #e4e6e8;
    --label: #f1f2f3;
    --brand-grey: #4a4a4c;
    --green: #1d6a34;
    --orange: #f7a823;
    --ring: #f4b44a;
    --white: #ffffff;
    --text-dark: #2b2b2b;
  }
  * { margin: 0; padding: 0; box-sizing: border-box; }
  html, body {
    width: 1000px; height: 1200px; overflow: hidden;
    background: var(--bg);
  }
  .label {
    position: relative;
    width: 1000px; height: 1200px;
    background: radial-gradient(ellipse at 49% 45%, var(--label) 0%, var(--bg) 72%);
    font-family: "Roboto", Arial, sans-serif;
    color: var(--text-dark);
  }
  .row {
    position: absolute; left: 0; width: 976px;
    text-align: center;
  }
  .brand-mark {
    position: absolute; top: 262px; left: 388px;
    width: 200px; height: 200px; border-radius: 50%;
    background: var(--orange);
  }
  .brand-name {
    top: 498px;
    font-weight: 700; font-size: 35px; letter-spacing: -0.2px;
    color: var(--brand-grey);
  }
  .product-name {
    top: 583px;
    font-family: "Tenor Sans", sans-serif;
    font-weight: 400; font-size: 60px; letter-spacing: 3px;
    color: var(--green);
    -webkit-text-stroke: 1.6px var(--green);
  }
  .product-type {
    top: 664px;
    font-family: "Dosis", sans-serif;
    font-weight: 500; font-size: 30px; letter-spacing: 1.5px;
    color: var(--green);
  }
  .divider {
    position: absolute; top: 716px; left: 371px;
    width: 233px; height: 2px; background: var(--green);
  }
  .tagline {
    top: 744px;
    font-family: "Roboto Condensed", sans-serif;
    font-weight: 700; font-size: 18.5px; letter-spacing: 1px;
    color: var(--green);
  }
  .features {
    position: absolute; top: 805px; left: 281px;
    display: flex; gap: 48px;
    list-style: none;
  }
  .feature {
    width: 104px;
    display: flex; flex-direction: column; align-items: center;
  }
  .feature-badge {
    width: 104px; height: 104px; border-radius: 50%;
    border: 2px solid var(--ring);
    background: rgba(255,255,255,0.55);
    display: flex; align-items: center; justify-content: center;
  }
  .feature-icon {
    width: 88px; height: 88px; border-radius: 50%;
    background: var(--orange);
    display: flex; align-items: center; justify-content: center;
  }
  .feature-icon svg { width: 56px; height: 56px; }
  .feature-label {
    margin-top: 18px;
    font-family: "Roboto Condensed", sans-serif;
    font-weight: 500; font-size: 17px; line-height: 1.3; text-align: center;
    color: var(--text-dark);
  }
  .net-weight {
    top: 1018px;
    font-family: "Roboto Condensed", sans-serif;
    font-weight: 500; font-size: 16px; letter-spacing: 0.4px;
    color: var(--text-dark);
  }
</style>
</head>
<body>
<main class="label">
  <span class="brand-mark"></span>
  <p class="row brand-name">Lanternmoss tea</p>

  <h1 class="row product-name">GUAYUSA</h1>
  <p class="row product-type">BLEND TEA</p>
  <div class="divider"></div>
  <p class="row tagline">PROVIDES CLEAN ENERGY TO THE BODY</p>

  <ul class="features">
    <li class="feature">
      <div class="feature-badge"><div class="feature-icon">
        <svg viewBox="0 0 56 56" role="img" aria-label="Steaming tea cup">
          <g fill="none" stroke="#fff" stroke-width="2.5" stroke-linecap="round">
            <path d="M22 6c-3 4 3 6 0 10M28 4c-3 4 3 6 0 10M34 6c-3 4 3 6 0 10"/>
          </g>
          <path d="M12 24h30v6c0 8-6 14-15 14S12 38 12 30z" fill="#fff"/>
          <path d="M42 27h3a5 5 0 0 1 0 10h-4" fill="none" stroke="#fff" stroke-width="3"/>
          <path d="M6 48h44" stroke="#fff" stroke-width="3" stroke-linecap="round"/>
        </svg>
      </div></div>
      <span class="feature-label">Coffee<br>Alternative</span>
    </li>
    <li class="feature">
      <div class="feature-badge"><div class="feature-icon">
        <svg viewBox="0 0 56 56" role="img" aria-label="Cacao pod">
          <path d="M28 12c9 0 13 10 13 22s-6 18-13 18-13-6-13-18 4-22 13-22z" fill="#fff"/>
          <g fill="none" stroke="#f7a823" stroke-width="1.8">
            <path d="M28 14v36M21 16c-3 8-3 26 1 33M35 16c3 8 3 26-1 33"/>
          </g>
          <path d="M28 12c0-4 2-7 5-8M31 8c4-4 9-3 10-2-3 4-7 4-10 2z" fill="#fff" stroke="#fff" stroke-width="2"/>
        </svg>
      </div></div>
      <span class="feature-label">Theobromine</span>
    </li>
    <li class="feature">
      <div class="feature-badge"><div class="feature-icon">
        <svg viewBox="0 0 56 56" role="img" aria-label="Two guayusa leaves">
          <path d="M26 46C10 44 4 28 8 10c14 2 22 14 18 36z" fill="#fff"/>
          <path d="M30 46c16-2 22-18 18-36-14 2-22 14-18 36z" fill="#fff"/>
          <g fill="none" stroke="#f7a823" stroke-width="1.6">
            <path d="M25 45C20 34 15 22 10 12M31 45c5-11 10-23 15-33"/>
          </g>
        </svg>
      </div></div>
      <span class="feature-label">100%<br>Guayusa</span>
    </li>
  </ul>

  <p class="row net-weight">NET WT. 113 oz (32 g)</p>
</main>
</body>
</html>
```